website conversion to Wordpress with an updated look and feel

Bright Torque Hub Limited is a company and an online presence, which promotes and sells a branded fuel additive product named “Valmix”.

The existing website is at www.brighttorquehub.co.uk

The site consists of static but attractive pages, a contact form, and most importantly a shopping page which is driven externally using shopvarn.com. Therefore e-commerce coding is NOT required as this task is performed by shopvarn via a plugin.

The website is 4 years old and we intend to revamp the graphics and the image of the company and the website to give it a modern “Windows 10” look!

Less text and less cluttering, Cleaner and easier navigations, bigger and clearer fonts. Simple message to put across to visitors/potential customers. Be creative.

The site needs to be simplified - the detail can/should still be there... But it can be placed deeper down or hidden by the use of dropdowns, callouts, etc.

A couple of good example styles we like are

https://www.brolavent.com/
http://www.4plumtoaster.com/en/#/welcome
https://www.tivoramp.com/

Some specific areas of attention.

homepage - This needs to really reflect the new look-and feel of the website. In addition the product we sell can be used in a number of applications - currently navigation to these different applications is through the moving banner. This needs to be changed. The major areas for access should be

Heating Oil
Vehicles
Marine
Generators

Technical requirements what we want:-
Wordpress (self hosted ) - currently Joomla based
Use of webfonts to improve typographic appearances
Shopvarn integration using plugin
Facebook/Twitter integration
Responsive design (Mobile friendly)
Search Engine friendly and some SEO optimisation
Google Analytics / Bing webmaster tracking

Target Market(s)

Owners of Olm branded range cookers and similar - our product fixes a fuel problem specific to these devices.

Also bulk fuel users looking to save money on their fuel costs - product improves fuel efficiency and reduces maintenance.

Industry/Entity Type

E-Commerce

Font styles to use
Sans Serif

Requirements
Must have
• Wordpress design
• Responsive design
• Simple "clean" look and feel
• Use of stock graphics
• a review of all current pages
Nice to have
• Social media integration - blog
• A forum to discuss the product and problems people experience with fuel

```html
<!DOCTYPE html>
<html lang="en">
<head>
<meta charset="utf-8">
<title>Bright Torque Hub Limited – Sections</title>
<link rel="stylesheet" href="https://fonts.googleapis.com/css2?family=Open+Sans:wght@300;400&display=swap">
<style>
  :root {
    --bar-dark: #4a4a4a;
    --brand-green: #64a233;
    --tile-grey: #e0e0e0;
    --icon-dark: #505050;
    --icon-light: #e2e2e2;
    --text-dark: #1f1f1f;
    --page-white: #ffffff;
    --page-mist: #ececec;
    --page-foot: #f1f8f9;
  }
  * { box-sizing: border-box; margin: 0; padding: 0; }
  html, body { width: 1200px; height: 608px; overflow: hidden; }
  body {
    font-family: "Open Sans", Arial, sans-serif;
    position: relative;
    background:
      linear-gradient(180deg, var(--page-mist) 0%, #f7f7f7 22%, var(--page-white) 40%, var(--page-white) 70%, var(--page-foot) 100%);
  }
  .top-bar {
    position: absolute; left: 0; top: 0; width: 1200px; height: 16px;
    background: var(--bar-dark);
  }
  .top-band {
    position: absolute; left: 0; top: 16px; width: 1200px; height: 14px;
    background: var(--brand-green);
  }
  .swoosh {
    position: absolute; left: 560px; top: 30px; width: 420px; height: 60px;
  }
  .section-tiles {
    position: absolute; left: 138px; top: 158px;
    display: flex; gap: 21px;
  }
  .tile {
    position: relative;
    width: 292px; height: 331px;
    background: var(--tile-grey);
    color: var(--text-dark);
    text-decoration: none;
  }
  .tile--wide { width: 301px; }
  .tile--active { background: var(--brand-green); }
  .tile-icon {
    position: absolute; left: 0; top: 0; width: 100%; height: 250px;
  }
  .tile-label {
    position: absolute; left: 0; right: 0; top: 262px;
    text-align: center;
    font-weight: 300; font-size: 28px; letter-spacing: 0.2px;
    text-transform: uppercase;
  }
  .bottom-band {
    position: absolute; left: 0; top: 582px; width: 1200px; height: 21px;
    background: var(--brand-green);
  }
</style>
</head>
<body>
  <div class="top-bar"></div>
  <div class="top-band"></div>
  <svg class="swoosh" viewBox="0 0 420 60" aria-hidden="true">
    <path d="M20 30 C120 5, 260 0, 400 -5 C280 10, 160 25, 20 30Z" fill="#ffffff" opacity="0.9"/>
    <path d="M180 45 C260 25, 340 12, 410 0" stroke="#ffffff" stroke-width="2" fill="none" opacity="0.8"/>
  </svg>

  <nav class="section-tiles">
    <a class="tile tile--active" href="#fuel-saving-tips">
      <svg class="tile-icon" viewBox="0 0 292 250" aria-hidden="true">
        <circle cx="124" cy="113" r="30" fill="var(--icon-light)"/>
        <circle cx="167" cy="92" r="27" fill="var(--icon-light)"/>
        <path d="M118 99 l8-5 v34 h-7 v-24 l-4 2z" fill="var(--brand-green)"/>
        <path d="M163 78 l8-5 v32 h-7 v-22 l-4 2z" fill="var(--brand-green)"/>
        <path d="M58 185 L100 172 C120 168 140 170 152 176 C162 181 150 192 138 190 L124 188 C135 192 148 195 160 190 L220 152 C230 146 240 156 232 164 L176 205 C160 216 140 218 120 214 L84 208 L66 210 Z" fill="var(--icon-light)"/>
      </svg>
      <span class="tile-label">Fule Saving Tips</span>
    </a>
    <a class="tile" href="#emmisions">
      <svg class="tile-icon" viewBox="0 0 292 250" aria-hidden="true">
        <path d="M78 118 C62 90 80 62 118 58 C124 86 110 114 78 118Z" fill="var(--icon-dark)"/>
        <path d="M88 124 C84 104 96 84 116 72" stroke="var(--tile-grey)" stroke-width="3" fill="none"/>
        <path d="M176 58 C208 68 220 100 204 138 C178 122 168 92 176 58Z" fill="var(--icon-dark)"/>
        <path d="M180 66 C196 90 200 112 198 132" stroke="var(--tile-grey)" stroke-width="3" fill="none"/>
        <path d="M96 158 C120 140 158 140 182 162 C160 188 122 192 96 158Z" fill="var(--icon-dark)"/>
        <path d="M108 160 C132 158 156 160 176 164" stroke="var(--tile-grey)" stroke-width="3" fill="none"/>
      </svg>
      <span class="tile-label">Emmisions</span>
    </a>
    <a class="tile tile--wide" href="#case-studies">
      <svg class="tile-icon" viewBox="0 0 301 250" aria-hidden="true">
        <rect x="106" y="62" width="104" height="128" rx="8" fill="var(--icon-dark)"/>
        <rect x="96" y="54" width="78" height="136" rx="8" fill="var(--icon-dark)"/>
        <path d="M150 66 L196 66 L196 176 L184 182 Z" fill="var(--tile-grey)"/>
        <g fill="var(--icon-dark)">
          <rect x="160" y="76" width="34" height="5" rx="2"/>
          <rect x="164" y="96" width="30" height="5" rx="2"/>
          <rect x="168" y="116" width="26" height="5" rx="2"/>
          <rect x="172" y="136" width="22" height="5" rx="2"/>
          <rect x="176" y="156" width="18" height="5" rx="2"/>
        </g>
      </svg>
      <span class="tile-label">Case Studies</span>
    </a>
  </nav>

  <div class="bottom-band"></div>
</body>
</html>
```